Real Estate Entrepreneur needs a business card

I am a real estate entrepreneur, I buy houses for investment purposes, I act as a real estate agent representing buyers and sellers in residential home transactions, I am a contractor that does a wide range of home repairs and construction. I'd like a design that can stick with me through the years as my business grows and morphs to fit any niche I decide to pursue as markets change.

Target Market(s)

Anyone with interest that may be related to real estate.

Industry/Entity Type

Real Estate

Contact Information for Business Card

A card that stands out and doesn't put me in any one box. My business will evolve over time and I need a card that can stay relevant.

Colors

Designer to choose colors to be used in the design.

Requirements
Must have
• Character
Nice to have
• I'm open
Should not have
• Cliche houses and hammers

```html
<!DOCTYPE html>
<html lang="en">
<head>
<meta charset="utf-8">
<title>Reid Harlow — Business Card</title>
<link rel="stylesheet" href="https://fonts.googleapis.com/css2?family=Lexend:wght@400;500&display=swap">
<style>
  :root {
    --backdrop-light: #4a4a4a;
    --backdrop-dark: #161616;
    --card: #232425;
    --ink: #ffffff;
    --accent: #e3232c;
  }
  * { margin: 0; padding: 0; box-sizing: border-box; }
  html, body { width: 1200px; height: 900px; overflow: hidden; }
  body {
    background: radial-gradient(ellipse at 85% 10%, var(--backdrop-light), var(--backdrop-dark) 70%);
    font-family: "Lexend", "Helvetica Neue", Arial, sans-serif;
    color: var(--ink);
    position: relative;
  }
  .card {
    position: absolute;
    left: 290px;
    width: 620px;
    height: 354px;
    background: var(--card);
    box-shadow: 0 14px 30px rgba(0, 0, 0, 0.55);
  }
  .card--front { top: 70px; }
  .card--back { top: 470px; }

  .brand-name {
    position: absolute;
    right: 44px;
    bottom: 36px;
    font-size: 58px;
    font-weight: 500;
    letter-spacing: 0;
    line-height: 1;
    color: var(--ink);
  }

  .contact-list {
    position: absolute;
    left: 38px;
    top: 34px;
    list-style: none;
    font-size: 18px;
    font-weight: 400;
    line-height: 1.36;
  }
  .accent-rule {
    position: absolute;
    left: 0;
    bottom: 62px;
    width: 405px;
    height: 3px;
    background: var(--accent);
  }
  .social-handle {
    position: absolute;
    left: 420px;
    bottom: 50px;
    font-size: 20px;
    font-weight: 400;
    display: flex;
    align-items: center;
    gap: 10px;
  }
  .social-handle .marker {
    width: 14px;
    height: 14px;
    border-radius: 50%;
    background: var(--ink);
  }
</style>
</head>
<body>
  <section class="card card--front" aria-label="Card front">
    <h1 class="brand-name">Reid Harlow</h1>
  </section>

  <section class="card card--back" aria-label="Card back">
    <ul class="contact-list">
      <li>(555) 214 - 6830 (Office)</li>
      <li>(555) 487 - 2051 (Cell)</li>
      <li>hello@reidharlow.com</li>
      <li>www.reidharlow.com</li>
    </ul>
    <div class="accent-rule"></div>
    <p class="social-handle">reidharlow / <span class="marker"></span></p>
  </section>
</body>
</html>
```